Need Business Card for our Indian Grocery Store

Industry/Entity Type

Grocery Store

Contact Information for Business Card

Manoj Baweja
Director

Store Locations:

Kellbrook
482 Elm Parade
P: 03 9172 5843

Marrowdale
613 Carlow Road
P: 03 9238 6014

email: kvtmarts@mailnest.example

Requirements
Must have
• Our logo Colours

```html
<!DOCTYPE html>
<html lang="en">
<head>
<meta charset="UTF-8">
<title>KVT Marts Business Card</title>
<link rel="stylesheet" href="https://fonts.googleapis.com/css2?family=Open+Sans:wght@400;600&display=swap">
<style>
  :root {
    --backdrop: #5c5c5c;
    --card-front: #84151a;
    --card-back: #ffffff;
    --brand-red: #e01e26;
    --ink: #1a1a1a;
    --white: #ffffff;
  }
  html, body {
    margin: 0;
    padding: 0;
    width: 1200px;
    height: 1200px;
    overflow: hidden;
    background: var(--backdrop);
    font-family: "Open Sans", Arial, sans-serif;
  }
  .canvas {
    position: relative;
    width: 1200px;
    height: 1200px;
  }
  .card {
    position: absolute;
    left: 240px;
    width: 720px;
    height: 419px;
    border-radius: 29px;
    overflow: hidden;
  }
  .card--front {
    top: 142px;
    background: var(--card-front);
  }
  .card--back {
    top: 638px;
    background: var(--card-back);
    color: var(--ink);
  }
  .brand-name {
    position: absolute;
    font-weight: 600;
    white-space: nowrap;
    letter-spacing: 1px;
  }
  .card--front .brand-name {
    left: 0;
    width: 720px;
    top: 118px;
    text-align: center;
    font-size: 64px;
    color: var(--white);
  }
  .card--front .email {
    position: absolute;
    left: 0;
    width: 720px;
    top: 362px;
    text-align: center;
    font-size: 22px;
    color: var(--ink);
  }
  .edge-tab {
    position: absolute;
    left: -14px;
    top: 48px;
    width: 28px;
    height: 28px;
    border-radius: 50%;
    background: var(--brand-red);
  }
  .person {
    position: absolute;
    left: 26px;
    top: 42px;
  }
  .person__name {
    margin: 0;
    font-size: 30px;
    font-weight: 400;
    line-height: 1.1;
  }
  .person__surname { color: var(--brand-red); }
  .person__role {
    margin: 2px 0 0;
    font-size: 23px;
    color: var(--brand-red);
  }
  .card--back .brand-name {
    right: 40px;
    top: 64px;
    font-size: 42px;
    color: var(--brand-red);
  }
  .divider {
    position: absolute;
    left: 26px;
    top: 176px;
  }
  .locations__title {
    position: absolute;
    left: 0;
    width: 720px;
    top: 190px;
    text-align: center;
    font-size: 23px;
    color: var(--brand-red);
  }
  .store {
    position: absolute;
    top: 212px;
    font-size: 24px;
    line-height: 37px;
  }
  .store p { margin: 0; }
  .store--left { left: 55px; }
  .store--right { right: 72px; text-align: right; }
  .card--back .email {
    position: absolute;
    left: 0;
    width: 720px;
    top: 352px;
    text-align: center;
    font-size: 23px;
  }
</style>
</head>
<body>
<main class="canvas">
  <section class="card card--front" aria-label="Card front">
    <div class="brand-name">KVT Marts</div>
    <div class="email">kvtmarts@mailnest.example</div>
  </section>

  <section class="card card--back" aria-label="Card back">
    <span class="edge-tab"></span>
    <div class="person">
      <h1 class="person__name">Manoj <span class="person__surname">Baweja</span></h1>
      <p class="person__role">Director</p>
    </div>
    <div class="brand-name">KVT Marts</div>

    <svg class="divider" width="668" height="8" viewBox="0 0 668 8" aria-hidden="true">
      <path d="M0 4 Q 180 -1 334 1.5 Q 520 4 668 4 Q 520 4.5 334 6.5 Q 180 9 0 4 Z" fill="var(--brand-red)"/>
    </svg>

    <div class="locations__title">Store Locations</div>
    <div class="store store--left">
      <p>Kellbrook</p>
      <p>482 Elm Parade</p>
      <p>&nbsp;P: 03 9172 5843</p>
    </div>
    <div class="store store--right">
      <p>Marrowdale</p>
      <p>613 Carlow Road</p>
      <p>P: 03 9238 6014</p>
    </div>
    <div class="email">kvtmarts@mailnest.example</div>
  </section>
</main>
</body>
</html>
```